Professional Document Wallet Design - Corporate Presentation Folder Design

Corporate Presentation Folder is known as a Document Wallet in Ireland.

This listing is for a design of a product called 'Document Wallets' - design for both inside and out. An example of the finished product is attached - 'preview document wallet.png'. This gives a clear example of what the document wallet looks like and for further details about this product you can visit this link.
http://www.presswerk-example.com/ie/group/double-gloss-lam-interlocking-presentation-folders
Attached "finish-image-1.jpg" gives an overview of the product outline as well as dimensions - also "preview document wallet"

'P10 template.indd' or 'P10 template.pdf' give the most detailed measurements of the product as these are the actual templates to be used in printing the product and therefore designs must be delivered on either of these.

Company Background

The client is a professional construction group and leads some of the largest construction jobs in the country for clients such as zentrix, novar and brelto to name a few.
The brief is to design a document wallet both sides that reflects well on their corporate clients, shows off their existing branding clearly and highlights their strengths completely.
The clients current branding can be seen at this address http://dunleavy.foxpintmedia.example/ but please be aware this website is still a work in progress.
An example of stationery styling liked by the client is found in the attached, Example of styling.pdf

Contents of the Design

As these document are a touch point for the company it is imperative that the following information is included.

1. The Company Logo
This must be clearly visible and the colouring around it enhance it's visibility. The logo should be to the fore and the design in no way should distract or detract attention from it.
2. Company Address and other contact details.
Address
Tullorren,
Carrowmeelan,
Castlerea,
Co. Roscommon

T: 094 9287403
E: info@dunleavygroup.example
W: www.dunleavygroup.example

3. Some images should be included and can be found at
https://files.example.com/folderview?id=0Q_XKcTmPwRaLdNbVfGhJsYtUeZo&usp=sharing
but stock images can be used if required to ensure the most professional look and feel for the project.

Printing
UV spot printing will be used on this printing and it is a requirement of the design to incorporate this into the finished article in some way. The document wallets are double sided so the same design should run throughout and consideration given to the user opening the wallet.
Updates

Target Market(s)

Professional corporate Clients

Industry/Entity Type

Product

Requirements
Must have
• Professional
• Striking
• Branding
• Logo
• Contact details
Nice to have
• A design surrounding the business card holder o the document wallet to enhance the area where the business card is held.

```html
<!DOCTYPE html>
<html lang="en">
<head>
<meta charset="utf-8">
<title>Dunleavy Group – Document Wallet Inside Spread</title>
<link href="https://fonts.googleapis.com/css2?family=Roboto:wght@400;700;900&display=swap" rel="stylesheet">
<style>
  :root {
    --backdrop: #f1efed;
    --panel-light: #e9ecec;
    --panel-mid: #d6dbdc;
    --panel-edge: #c8cecf;
    --brand-violet: #3b3192;
    --brand-violet-deep: #2f2678;
    --ink: #111111;
    --ink-soft: #333333;
    --card: #fbfbfb;
    --photo-sky: #b9cbd6;
    --photo-steel: #7f8b92;
    --photo-glass: #a7b4bb;
  }
  html, body {
    margin: 0;
    width: 1200px;
    height: 857px;
    overflow: hidden;
    background: var(--backdrop);
    font-family: "Roboto", Arial, sans-serif;
  }
  .spread {
    position: absolute;
    left: 120px;
    top: 98px;
    width: 960px;
    height: 660px;
    display: flex;
    box-shadow: 0 18px 40px rgba(0,0,0,0.12);
  }
  .panel {
    position: relative;
    width: 480px;
    height: 660px;
    overflow: hidden;
    background: radial-gradient(ellipse at 50% 40%, var(--panel-light) 0%, var(--panel-mid) 75%, var(--panel-edge) 100%);
  }
  .panel--left { border-right: 1px solid #c4c9ca; }

  .lockup {
    position: absolute;
    display: flex;
    flex-direction: column;
    align-items: flex-start;
    color: var(--ink);
  }
  .brand {
    display: flex;
    align-items: center;
    gap: 10px;
  }
  .brand__mark {
    flex: none;
    width: 44px;
    height: 44px;
    background: var(--brand-violet);
  }
  .brand__name {
    font-weight: 900;
    font-size: 27px;
    letter-spacing: -0.5px;
    line-height: 1;
    white-space: nowrap;
  }
  .tagline {
    margin: 6px 0 0;
    padding-top: 4px;
    border-top: 1px solid var(--ink);
    font-size: 7.5px;
    font-weight: 400;
    letter-spacing: 0.2px;
    color: var(--ink-soft);
    white-space: nowrap;
  }
  .panel--left .lockup { left: 145px; top: 74px; }
  .panel--right .lockup { left: 110px; top: 322px; }
  .panel--right .brand__mark { width: 54px; height: 54px; }
  .panel--right .brand__name { font-size: 32px; }
  .panel--right .tagline { font-size: 9px; }

  .photo-strip {
    position: absolute;
    left: 50px;
    top: 150px;
    width: 380px;
    height: 150px;
  }
  .intro {
    position: absolute;
    left: 95px;
    top: 330px;
    width: 300px;
    margin: 0;
    font-size: 8.5px;
    font-weight: 700;
    line-height: 1.35;
    text-align: justify;
    color: var(--ink);
  }

  .pocket {
    position: absolute;
    left: 0;
    bottom: 0;
    width: 480px;
    height: 250px;
  }
  .business-card {
    position: absolute;
    left: 140px;
    top: 488px;
    width: 200px;
    height: 112px;
    box-sizing: border-box;
    padding: 14px 16px 0 18px;
    background: var(--card);
    clip-path: polygon(0 0, 93% 0, 100% 12%, 100% 88%, 93% 100%, 0 100%);
    box-shadow: 0 2px 6px rgba(0,0,0,0.25);
    color: var(--ink);
  }
  .business-card .brand { gap: 5px; }
  .business-card .brand__mark { width: 16px; height: 16px; }
  .business-card .brand__name { font-size: 12px; letter-spacing: 0; }
  .business-card .tagline { font-size: 5.5px; margin-top: 4px; padding-top: 3px; }
  .contact {
    margin: 7px 0 0;
    font-style: normal;
    font-size: 6.5px;
    line-height: 1.45;
    color: var(--ink-soft);
  }
</style>
</head>
<body>
  <main class="spread">
    <section class="panel panel--left">
      <div class="lockup">
        <div class="brand">
          <span class="brand__mark"></span>
          <span class="brand__name">Dunleavy Group</span>
        </div>
        <p class="tagline">Construction–Carpentry–Mechanical–Maintenance</p>
      </div>

      <svg class="photo-strip" viewBox="0 0 380 150" role="img" aria-label="Three angled photographs of modern glass and steel building facades">
        <defs>
          <linearGradient id="photoSky" x1="0" y1="0" x2="1" y2="1">
            <stop offset="0" stop-color="var(--photo-sky)"/>
            <stop offset="1" stop-color="#e4ecef"/>
          </linearGradient>
          <linearGradient id="photoSteel" x1="0" y1="0" x2="1" y2="1">
            <stop offset="0" stop-color="#9aa4aa"/>
            <stop offset="1" stop-color="var(--photo-steel)"/>
          </linearGradient>
          <linearGradient id="photoGlass" x1="0" y1="0" x2="1" y2="1">
            <stop offset="0" stop-color="#dde4e6"/>
            <stop offset="1" stop-color="var(--photo-glass)"/>
          </linearGradient>
        </defs>
        <polygon points="0,18 135,18 120,100 0,100" fill="url(#photoSky)"/>
        <polygon points="150,10 255,45 215,150 115,115" fill="url(#photoSteel)"/>
        <polygon points="270,40 370,40 380,148 245,148" fill="url(#photoGlass)"/>
      </svg>

      <p class="intro">Lorem ipsum dolor sit amet, consectetur adipisicing elit, sed do eiusmod tempor incididunt ut labore et dolore magna aliqua. Ut enim ad minim veniam, quis nostrud exercitation. Lorem ipsum dolor sit amet, consectetur adipisicing elit, sed do eiusmod tempor incididunt ut labore et dolore magna aliqua. Ut enim ad minim veniam, quis nostrud exercitation. Lorem ipsum dolor sit amet, consectetur adipisicing elit, sed do eiusmod tempor incididunt ut labore et dolore magna aliqua. Ut enim ad minim veniam, quis nostrud exercitation. Lorem ipsum dolor sit amet, consectetur adipisicing elit, sed do eiusmod tempor incididunt ut labore et dolore magna aliqua. Ut enim ad minim veniam, quis nostrud exercitation.</p>
    </section>

    <section class="panel panel--right">
      <div class="lockup">
        <div class="brand">
          <span class="brand__mark"></span>
          <span class="brand__name">Dunleavy Group</span>
        </div>
        <p class="tagline">Construction–Carpentry–Mechanical–Maintenance</p>
      </div>

      <svg class="pocket" viewBox="0 0 480 250" aria-hidden="true">
        <defs>
          <linearGradient id="pocketFill" x1="0" y1="0" x2="0" y2="1">
            <stop offset="0" stop-color="var(--brand-violet)"/>
            <stop offset="1" stop-color="var(--brand-violet-deep)"/>
          </linearGradient>
        </defs>
        <path d="M0,250 L0,60 Q0,0 60,0 L480,0 L480,250 Z" fill="url(#pocketFill)"/>
      </svg>

      <div class="business-card">
        <div class="brand">
          <span class="brand__mark"></span>
          <span class="brand__name">Dunleavy Group</span>
        </div>
        <p class="tagline">Construction–Carpentry–Mechanical–Maintenance</p>
        <address class="contact">
          Tullorren, Carrowmeelan, Castlerea, Co. Roscommon<br>
          T: 094 9287403<br>
          E: info@dunleavygroup.example<br>
          W: www.dunleavygroup.example
        </address>
      </div>
    </section>
  </main>
</body>
</html>
```